Koveli Seafood Shipping Packaging Re-Design

We need a packaging (Shipping Carton) design for our Seafood Products (FROZEN). We already have a basic packaging design which we prefer to have a modern touch on it.
Spec :
1. It must show our logo (Attached), note that the text of "KOVELI" which accompany the logo is optional, it can be omitted & showing only the logo.
2. Main color is Blue
3. Our carton is regular shipping box with dimension L43cm x W 27cm x H 16cm.
4. Our material of Carton is both Brown & White Kraft Paperboard, so the design should look nice in both material.

Attached our Logo and packaging design.

Target Market(s)

Frozen Seafood Distributor & Seafood Buyer

Industry/Entity Type

Food Production

Requirements
Must have
• 1. Must Show our Logo
• 2. Main Color of the Text/Logo is Blue
• 3. On the side of the packaging / Carton must show two box of CODE & SIZE
• 4. Must Show these icons :
• a. Handle with Care
• b. Maximum Stackable 10 Carton
• c. Recyleable Material
• d. Protect from the Water/Rain
Nice to have
• Would prefer to have a modern design

```html
<!DOCTYPE html>
<html lang="en">
<head>
<meta charset="utf-8">
<title>Koveli Frozen Seafood Shipping Carton – Dielines</title>
<link href="https://fonts.googleapis.com/css2?family=Nunito+Sans:wght@600;700;800&display=swap" rel="stylesheet">
<style>
  :root {
    --bg: #eceef1;
    --navy: #1b2d69;
    --blue: #2f5fa6;
    --wave-light: #c9d7ee;
    --white-board: #ffffff;
    --white-line: #c6cbe0;
    --kraft-board: #d4b083;
    --kraft-line: #b8946a;
  }
  * { box-sizing: border-box; margin: 0; padding: 0; }
  html, body { width: 960px; height: 1200px; overflow: hidden; }
  body {
    background: var(--bg);
    font-family: "Nunito Sans", Arial, sans-serif;
    color: var(--navy);
    position: relative;
  }
  .dieline {
    position: absolute;
    left: 38px;
    width: 884px;
    height: 264px;
    --board: var(--white-board);
    --line: var(--white-line);
  }
  .dieline--white { top: 272px; }
  .dieline--kraft { top: 660px; --board: var(--kraft-board); --line: var(--kraft-line); }

  .glue-tab { position: absolute; left: 0; top: 82px; width: 21px; height: 98px; }

  .panels {
    position: absolute;
    left: 20px; top: 0;
    display: grid;
    grid-template-columns: 266px 166px 264px 164px;
    grid-template-rows: 82px 98px 84px;
    gap: 2px;
  }
  .panel {
    position: relative;
    background: var(--board);
    outline: 1px solid var(--line);
    overflow: hidden;
  }

  .wave-band {
    position: absolute; left: 0; right: 0;
    height: 16px;
  }
  .wave-band--top { top: 0; background: linear-gradient(to bottom, var(--blue), var(--wave-light) 85%, transparent); opacity: .85; }
  .wave-band--bottom { bottom: 0; background: linear-gradient(to top, var(--blue), var(--wave-light) 85%, transparent); opacity: .85; }

  .brand {
    position: absolute; left: 0; right: 0; top: 14px;
    display: flex; align-items: center; justify-content: center; gap: 8px;
  }
  .brand--flipped { top: 20px; transform: rotate(180deg); }
  .brand__dot { width: 30px; height: 30px; border-radius: 50%; background: var(--blue); }
  .brand__name { font-weight: 700; font-size: 22px; letter-spacing: 2px; color: var(--navy); }

  .label-pair { display: flex; gap: 10px; }
  .label-box {
    border: 1.5px solid var(--navy);
    border-radius: 4px;
    overflow: hidden;
  }
  .label-box__head {
    background: var(--navy); color: #fff;
    font-weight: 800; letter-spacing: .5px;
    padding-left: 6px;
  }

  .flap-labels { position: absolute; left: 83px; top: 25px; }
  .flap-labels .label-pair { gap: 9px; }
  .flap-labels .label-box { width: 45px; height: 24px; border-width: 1px; border-radius: 3px; }
  .flap-labels .label-box__head { font-size: 4px; line-height: 5px; padding-left: 4px; }
  .temp-pill {
    margin: 8px 0 0 24px;
    width: 52px; height: 11px; border-radius: 6px;
    background: var(--navy); color: #fff;
    font-size: 7px; font-weight: 700; line-height: 11px; text-align: center;
  }

  .side-labels { position: absolute; left: 12px; top: 8px; }
  .side-labels .label-box { width: 66px; height: 62px; }
  .side-labels .label-box__head { font-size: 9px; line-height: 12px; }
  .care-icons {
    position: absolute; left: 0; right: 0; top: 74px;
    display: flex; justify-content: center; gap: 5px;
  }
  .care-icons svg { width: 16px; height: 16px; }
</style>
</head>
<body>

<svg width="0" height="0" style="position:absolute" aria-hidden="true">
  <defs>
    <symbol id="icon-rain" viewBox="0 0 20 20">
      <circle cx="10" cy="10" r="9" fill="none" stroke="#1b2d69" stroke-width="1.3"/>
      <path d="M4.5 10 A5.5 5 0 0 1 15.5 10 Z" fill="#1b2d69"/>
      <path d="M10 10 V14.5 A1.3 1.3 0 0 1 7.5 14.5" fill="none" stroke="#1b2d69" stroke-width="1.2"/>
      <path d="M6 4.5 v1.3 M10 3.5 v1 M14 4.5 v1.3" stroke="#1b2d69" stroke-width="1"/>
    </symbol>
    <symbol id="icon-care" viewBox="0 0 20 20">
      <circle cx="10" cy="10" r="9" fill="none" stroke="#1b2d69" stroke-width="1.3"/>
      <path d="M6.5 5.5 h7 l-1 5 a2.5 2.5 0 0 1 -5 0 Z" fill="#1b2d69"/>
      <path d="M10 13 v2.5 M7.5 15.5 h5" stroke="#1b2d69" stroke-width="1.2"/>
    </symbol>
    <symbol id="icon-stack" viewBox="0 0 20 20">
      <circle cx="10" cy="10" r="9" fill="none" stroke="#1b2d69" stroke-width="1.3"/>
      <text x="10" y="10.5" text-anchor="middle" font-family="Nunito Sans, sans-serif" font-weight="800" font-size="7" fill="#1b2d69">10</text>
      <path d="M6 12.5 h8 M6 14.5 h8" stroke="#1b2d69" stroke-width="1"/>
    </symbol>
    <symbol id="icon-recycle" viewBox="0 0 20 20">
      <circle cx="10" cy="10" r="9" fill="none" stroke="#1b2d69" stroke-width="1.3"/>
      <path d="M10 5 L13.5 11 M12.5 13.5 H6.5 M5.5 11 L9 5" fill="none" stroke="#1b2d69" stroke-width="1.4"/>
      <path d="M13.5 11 l.8 -2.2 M6.5 13.5 l1.8 1.4 M9 5 l-2.2 .5" stroke="#1b2d69" stroke-width="1.2"/>
    </symbol>
  </defs>
</svg>

<!-- Two identical carton dielines: white board and brown kraft board -->
<section class="dieline dieline--white" aria-label="Carton dieline on white board">
  <svg class="glue-tab" viewBox="0 0 21 98" aria-hidden="true"><polygon points="21,0 4,6 4,92 21,98" fill="var(--board)" stroke="var(--line)"/></svg>
  <div class="panels">
    <div class="panel flap">
      <div class="wave-band wave-band--top" role="img" aria-label="Blue ocean wave ornament"></div>
      <div class="flap-labels">
        <div class="label-pair">
          <div class="label-box"><div class="label-box__head">CODE 代码</div></div>
          <div class="label-box"><div class="label-box__head">SIZE 规格</div></div>
        </div>
        <div class="temp-pill">❄ -18℃</div>
      </div>
    </div>
    <div class="panel flap"></div>
    <div class="panel flap">
      <div class="wave-band wave-band--top" role="img" aria-label="Blue ocean wave ornament"></div>
      <div class="brand brand--flipped"><span class="brand__dot"></span><span class="brand__name">KOVELI</span></div>
    </div>
    <div class="panel flap"></div>

    <div class="panel long-side">
      <div class="brand"><span class="brand__dot"></span><span class="brand__name">KOVELI</span></div>
      <div class="wave-band wave-band--bottom" role="img" aria-label="Blue ocean wave ornament"></div>
    </div>
    <div class="panel short-side">
      <div class="side-labels label-pair">
        <div class="label-box"><div class="label-box__head">CODE 代码</div></div>
        <div class="label-box"><div class="label-box__head">SIZE 规格</div></div>
      </div>
      <div class="care-icons">
        <svg role="img" aria-label="Keep dry"><use href="#icon-rain"/></svg>
        <svg role="img" aria-label="Handle with care"><use href="#icon-care"/></svg>
        <svg role="img" aria-label="Stack maximum 10"><use href="#icon-stack"/></svg>
        <svg role="img" aria-label="Recyclable"><use href="#icon-recycle"/></svg>
      </div>
    </div>
    <div class="panel long-side">
      <div class="brand"><span class="brand__dot"></span><span class="brand__name">KOVELI</span></div>
      <div class="wave-band wave-band--bottom" role="img" aria-label="Blue ocean wave ornament"></div>
    </div>
    <div class="panel short-side">
      <div class="side-labels label-pair">
        <div class="label-box"><div class="label-box__head">CODE 代码</div></div>
        <div class="label-box"><div class="label-box__head">SIZE 规格</div></div>
      </div>
      <div class="care-icons">
        <svg role="img" aria-label="Keep dry"><use href="#icon-rain"/></svg>
        <svg role="img" aria-label="Handle with care"><use href="#icon-care"/></svg>
        <svg role="img" aria-label="Stack maximum 10"><use href="#icon-stack"/></svg>
        <svg role="img" aria-label="Recyclable"><use href="#icon-recycle"/></svg>
      </div>
    </div>

    <div class="panel flap"></div>
    <div class="panel flap"></div>
    <div class="panel flap"></div>
    <div class="panel flap"></div>
  </div>
</section>

<section class="dieline dieline--kraft" aria-label="Carton dieline on brown kraft board">
  <svg class="glue-tab" viewBox="0 0 21 98" aria-hidden="true"><polygon points="21,0 4,6 4,92 21,98" fill="var(--board)" stroke="var(--line)"/></svg>
  <div class="panels">
    <div class="panel flap">
      <div class="wave-band wave-band--top" role="img" aria-label="Blue ocean wave ornament"></div>
      <div class="flap-labels">
        <div class="label-pair">
          <div class="label-box"><div class="label-box__head">CODE 代码</div></div>
          <div class="label-box"><div class="label-box__head">SIZE 规格</div></div>
        </div>
        <div class="temp-pill">❄ -18℃</div>
      </div>
    </div>
    <div class="panel flap"></div>
    <div class="panel flap">
      <div class="wave-band wave-band--top" role="img" aria-label="Blue ocean wave ornament"></div>
      <div class="brand brand--flipped"><span class="brand__dot"></span><span class="brand__name">KOVELI</span></div>
    </div>
    <div class="panel flap"></div>

    <div class="panel long-side">
      <div class="brand"><span class="brand__dot"></span><span class="brand__name">KOVELI</span></div>
      <div class="wave-band wave-band--bottom" role="img" aria-label="Blue ocean wave ornament"></div>
    </div>
    <div class="panel short-side">
      <div class="side-labels label-pair">
        <div class="label-box"><div class="label-box__head">CODE 代码</div></div>
        <div class="label-box"><div class="label-box__head">SIZE 规格</div></div>
      </div>
      <div class="care-icons">
        <svg role="img" aria-label="Keep dry"><use href="#icon-rain"/></svg>
        <svg role="img" aria-label="Handle with care"><use href="#icon-care"/></svg>
        <svg role="img" aria-label="Stack maximum 10"><use href="#icon-stack"/></svg>
        <svg role="img" aria-label="Recyclable"><use href="#icon-recycle"/></svg>
      </div>
    </div>
    <div class="panel long-side">
      <div class="brand"><span class="brand__dot"></span><span class="brand__name">KOVELI</span></div>
      <div class="wave-band wave-band--bottom" role="img" aria-label="Blue ocean wave ornament"></div>
    </div>
    <div class="panel short-side">
      <div class="side-labels label-pair">
        <div class="label-box"><div class="label-box__head">CODE 代码</div></div>
        <div class="label-box"><div class="label-box__head">SIZE 规格</div></div>
      </div>
      <div class="care-icons">
        <svg role="img" aria-label="Keep dry"><use href="#icon-rain"/></svg>
        <svg role="img" aria-label="Handle with care"><use href="#icon-care"/></svg>
        <svg role="img" aria-label="Stack maximum 10"><use href="#icon-stack"/></svg>
        <svg role="img" aria-label="Recyclable"><use href="#icon-recycle"/></svg>
      </div>
    </div>

    <div class="panel flap"></div>
    <div class="panel flap"></div>
    <div class="panel flap"></div>
    <div class="panel flap"></div>
  </div>
</section>

</body>
</html>
```